elearning course template

Our company has a variety of elearning courses. We are currently redesigning the courses and are looking for a new layout for the online learning courses. The layout should be 800x600 and it needs to incorporate the following elements:
1. Course Name
2. Chapter Name
3. Page name
4. Our company logo (see attached file)
5. Navigation bar that includes:
- Next / back buttons
- Page count
- Audio control bar (see attached file)
- Menu items that include: "Menu, Transcript, Resources"
9. Exit button (may be included on the navigation bar if appropriate)
10. Content area must be 775 wide x 442 high

We would like to see designs that use our company colors, blue (RGB 0,69,144) and orange (RGB 222, 111, 51) and dark gray. We're looking for a solution that is clean, crisp and very user friendly. We'd also like to see a little dimension in the layout, we feel that our current layout is very "flat".

You can find out more about our company at www.fernwick-lro.com.

Industry/Entity Type

Graphic Design

```html
<!DOCTYPE html>
<html lang="en">
<head>
<meta charset="utf-8">
<title>eLearning Course Template</title>
<link rel="stylesheet" href="https://fonts.googleapis.com/css2?family=Exo+2:wght@400;500&family=PT+Sans:wght@400;700&display=swap">
<style>
  :root {
    --brand-blue: #004590;
    --brand-blue-dark: #0b2f5e;
    --brand-blue-deep: #0a2346;
    --brand-orange: #de6f33;
    --brand-orange-light: #f39a5c;
    --dark-gray: #3a3a3a;
    --frame-gray: #8a8a8a;
    --page-bg: #ffffff;
  }
  html, body {
    margin: 0;
    padding: 0;
    width: 1200px;
    height: 1148px;
    overflow: hidden;
    background: var(--page-bg);
  }
  .course-shell {
    display: block;
    width: 1200px;
    height: 1148px;
  }
  .course-title {
    font-family: "Exo 2", sans-serif;
    font-size: 27px;
    fill: #ffffff;
    letter-spacing: 0.5px;
  }
  .chapter-label, .page-label {
    font-family: "PT Sans", sans-serif;
    font-size: 18px;
    fill: var(--brand-orange);
  }
  .content-label {
    font-family: "Exo 2", sans-serif;
    font-size: 26px;
    fill: var(--brand-orange);
  }
  .brand-name {
    font-family: "PT Sans", sans-serif;
    font-weight: 700;
    font-size: 9px;
    fill: var(--brand-blue);
  }
  .page-count {
    font-family: "PT Sans", sans-serif;
    font-size: 7px;
    fill: var(--dark-gray);
  }
  .nav-label {
    font-family: "Exo 2", sans-serif;
    font-size: 10px;
    fill: #111111;
  }
  .header-band { fill: var(--brand-blue); }
  .content-frame { fill: #ffffff; stroke: var(--frame-gray); stroke-width: 1; }
  .nav-button { fill: url(#orangeFace); stroke: #a9491b; stroke-width: 0.6; }
  .icon-stroke { fill: none; stroke: var(--brand-blue-dark); stroke-width: 2; stroke-linecap: round; }
</style>
</head>
<body>
<svg class="course-shell" viewBox="0 0 880 842" xmlns="http://www.w3.org/2000/svg">
  <defs>
    <linearGradient id="orangeFace" x1="0" y1="0" x2="0" y2="1">
      <stop offset="0" stop-color="#f6a56a"/>
      <stop offset="0.5" stop-color="#de6f33"/>
      <stop offset="1" stop-color="#c85a22"/>
    </linearGradient>
    <linearGradient id="headerShade" x1="0" y1="0" x2="0" y2="1">
      <stop offset="0" stop-color="#0a559f"/>
      <stop offset="1" stop-color="#003a78"/>
    </linearGradient>
    <radialGradient id="footerGlow" cx="0.4" cy="0.2" r="0.8">
      <stop offset="0" stop-color="#3f6aa0"/>
      <stop offset="0.5" stop-color="#1b3f72"/>
      <stop offset="1" stop-color="#0a2346"/>
    </radialGradient>
    <linearGradient id="trackShade" x1="0" y1="0" x2="0" y2="1">
      <stop offset="0" stop-color="#ffffff"/>
      <stop offset="1" stop-color="#d6d6d6"/>
    </linearGradient>
  </defs>

  <!-- Header band -->
  <path class="header-band" fill="url(#headerShade)"
        d="M201,14 H580 A20.5,20.5 0 0 1 580,55 H262 Q214,56 201,96 Z"/>

  <!-- Exit button -->
  <g class="exit-button">
    <rect x="208" y="25" width="22" height="21" rx="3" class="nav-button"/>
    <path d="M213,30 L225,41 M225,30 L213,41" stroke="var(--brand-blue-dark)" stroke-width="2.6" stroke-linecap="round"/>
  </g>
  <!-- Settings button -->
  <g class="settings-button">
    <rect x="244" y="25" width="21" height="21" rx="3" class="nav-button"/>
    <circle cx="254.5" cy="35.5" r="5.5" fill="none" stroke="var(--brand-blue-dark)" stroke-width="2.4" stroke-dasharray="2 1.2"/>
    <circle cx="254.5" cy="35.5" r="2" fill="var(--brand-blue-dark)"/>
  </g>

  <text class="course-title" x="455" y="45" text-anchor="middle">Course Name</text>

  <!-- Company name -->
  <g class="brand">
    <circle cx="676" cy="30" r="8" fill="var(--brand-orange)"/>
    <text class="brand-name" x="676" y="52" text-anchor="middle">Fernwick LRO</text>
  </g>

  <text class="chapter-label" x="243" y="80">Chapter Name</text>
  <text class="page-label" x="672" y="80" text-anchor="end">Page Name</text>

  <!-- Footer band -->
  <path role="img" aria-label="Blue technical line pattern backdrop" fill="url(#footerGlow)"
        d="M201,275 Q205,349 290,351 H711 V437 H201 Z"/>

  <!-- Content area -->
  <rect class="content-frame" x="244" y="91" width="428" height="243"/>
  <text class="content-label" x="441" y="114" text-anchor="middle">Content area</text>

  <!-- Audio / progress bar -->
  <rect x="293" y="341" width="336" height="5" rx="2.5" fill="#9a9a9a" opacity="0.5"/>
  <rect x="292" y="339" width="335" height="5" rx="2.5" fill="url(#trackShade)" stroke="#bdbdbd" stroke-width="0.4"/>
  <rect x="292" y="339" width="66" height="5" rx="2.5" fill="var(--brand-orange)"/>
  <text class="page-count" x="643" y="344">10/29</text>

  <!-- Back button -->
  <g class="back-button">
    <rect x="214" y="386" width="38" height="27" rx="3" class="nav-button"/>
    <path d="M219,399.5 L230,391 V396 H246 V403 H230 V408 Z" fill="none" stroke="var(--brand-blue-dark)" stroke-width="1.4" stroke-linejoin="round"/>
  </g>
  <!-- Next button -->
  <g class="next-button">
    <rect x="661" y="386" width="38" height="27" rx="3" class="nav-button"/>
    <path d="M694,399.5 L683,391 V396 H667 V403 H683 V408 Z" fill="none" stroke="var(--brand-blue-dark)" stroke-width="1.4" stroke-linejoin="round"/>
  </g>

  <!-- Menu items -->
  <g class="menu-item">
    <rect x="274" y="399" width="87" height="14" class="nav-button"/>
    <text class="nav-label" x="317.5" y="410" text-anchor="middle">Menu</text>
  </g>
  <g class="menu-item">
    <rect x="406" y="399" width="87" height="14" class="nav-button"/>
    <text class="nav-label" x="449.5" y="410" text-anchor="middle">Resources</text>
  </g>
  <g class="menu-item">
    <rect x="549" y="399" width="87" height="14" class="nav-button"/>
    <text class="nav-label" x="592.5" y="410" text-anchor="middle">Transcript</text>
  </g>
</svg>
</body>
</html>
```